Quenly - Property Management Company Listings - PSD / uncoded only

Our site simply connects property owners with property managers. I’m asking you to create 2 pages, 1 homepage and 1 page that lists of property management companies. Build with Responsive Design in mind. PSD/uncoded files only. Help us create a great site!
Example competitor sites:
http://www.everyestatehelpers.example/
http://www.tendyourlots.example/
Inspired by these sites:
http://www.gravlet.example/
http://www.hornbrisk.example/
http://www.coinvex.example/
https://www.lanehive.example/
I've attached the logo as well as 2 picture files that you can consider using.
• Quenly Logo Colors: Yellow: HTML code: #FBC30A, RGB code: R: 251 G: 195 B: 10 Grey: HTML code: #4E4C4D, RGB code: R: 78 G: 76 B: 77
• The picture files are optional.
o One picture is of houses and neighborhood.
o The other is of a professional woman on the phone. Please do not use the professional woman as a large primary image. You can use the professional woman photo as a smaller photo and not the main photo.
• Please bring your own pictures and graphics too. Don't feel like you need to use mine.
Thank you!
Industry/Entity Type
Property Management

```html
<!DOCTYPE html>
<html lang="en">
<head>
<meta charset="utf-8">
<title>Quenly – Find your Local Property Manager</title>
<link href="https://fonts.googleapis.com/css2?family=Roboto:wght@400;500;700&display=swap" rel="stylesheet">
<style>
  :root {
    --brand-yellow: #fbc30a;
    --brand-grey: #4e4c4d;
    --text-dark: #3f3f3f;
    --white: #ffffff;
    --panel-yellow: rgba(251, 205, 10, 0.86);
    --button-dark: #3a3a3a;
  }
  * { box-sizing: border-box; margin: 0; padding: 0; }
  html, body { width: 1200px; height: 1001px; overflow: hidden; }
  body {
    position: relative;
    font-family: "Roboto", Arial, sans-serif;
    background: var(--white);
    color: var(--text-dark);
  }
  .site-header {
    position: absolute; left: 0; top: 0; width: 1200px; height: 62px;
    background: linear-gradient(#ffffff, #f1f1f1);
    border-bottom: 1px solid #dcdcdc;
  }
  .brand {
    position: absolute; left: 70px; top: 10px;
    display: flex; align-items: center; gap: 8px;
  }
  .brand-mark { width: 14px; height: 14px; background: var(--brand-yellow); }
  .brand-name {
    font-size: 34px; font-weight: 700; color: var(--brand-grey);
    line-height: 40px; letter-spacing: -0.5px;
  }
  .tagline {
    position: absolute; right: 55px; top: 18px;
    font-size: 19px; font-weight: 500; color: var(--text-dark);
  }
  .tagline span { color: var(--brand-yellow); }

  .hero {
    position: absolute; left: 0; top: 62px; width: 1200px; height: 638px;
  }
  .hero-photo {
    position: absolute; inset: 0;
    background:
      radial-gradient(ellipse at 50% 45%, rgba(0,0,0,0.05), rgba(0,0,0,0.35)),
      linear-gradient(170deg, #5d7a3e 0%, #6f6a5e 20%, #7d7468 45%, #6c665c 65%, #55644a 85%, #4a5640 100%);
  }
  .hero-title {
    position: absolute; left: 0; right: 0; top: 193px;
    text-align: center; color: var(--white);
    font-size: 35px; font-weight: 500;
    text-shadow: 0 2px 4px rgba(0,0,0,0.5);
  }
  .search-panel {
    position: absolute; left: 231px; top: 276px; width: 732px; height: 90px;
    background: var(--panel-yellow);
    box-shadow: 0 2px 6px rgba(0,0,0,0.25);
  }
  .field-label {
    position: absolute; top: 13px; font-size: 13px; color: var(--text-dark);
  }
  .label-type { left: 51px; }
  .label-zip { left: 413px; }
  .select-box {
    position: absolute; left: 38px; top: 35px; width: 342px; height: 40px;
    background: var(--white); border: 1px solid #ddd; border-radius: 2px;
    font-size: 13px; color: #666; padding: 0 13px; line-height: 38px;
  }
  .select-box::after {
    content: ""; position: absolute; right: 16px; top: 17px;
    border: 4px solid transparent; border-top: 4px solid #333;
  }
  .zip-input {
    position: absolute; left: 400px; top: 35px; width: 116px; height: 40px;
    background: var(--white); border: 1px solid #ddd; border-radius: 2px;
  }
  .search-button {
    position: absolute; left: 535px; top: 35px; width: 158px; height: 40px;
    background: var(--button-dark); border-radius: 2px; color: var(--white);
    font-size: 15px; font-weight: 500;
    display: flex; align-items: center; justify-content: center; gap: 9px;
  }
  .hero-note {
    position: absolute; left: 0; right: 0; top: 377px;
    text-align: center; font-size: 15px; color: var(--brand-yellow);
    text-shadow: 0 1px 2px rgba(0,0,0,0.4);
  }

  .steps-heading {
    position: absolute; left: 0; right: 0; top: 760px;
    text-align: center; font-size: 26px; color: var(--text-dark);
  }
  .steps-heading span { color: var(--brand-yellow); }
  .step-icon {
    position: absolute; top: 858px; width: 88px; height: 88px;
    border-radius: 50%; border: 4px solid var(--brand-grey);
    display: flex; align-items: center; justify-content: center;
  }
  .step-icon::before {
    content: ""; position: absolute; inset: 2px;
    border-radius: 50%; border: 3px solid var(--brand-yellow);
  }
  .step-icon svg { position: relative; }
  .step-arrow { position: absolute; top: 892px; }
  .step-caption {
    position: absolute; top: 967px; width: 360px;
    text-align: center; font-size: 15px; color: var(--text-dark);
  }
</style>
</head>
<body>
  <header class="site-header">
    <div class="brand">
      <span class="brand-mark"></span>
      <span class="brand-name">quenly</span>
    </div>
    <p class="tagline">Property Management Solutions, <span>Simplified.</span></p>
  </header>

  <section class="hero">
    <div class="hero-photo" role="img" aria-label="Aerial photo of a suburban neighbourhood with two-storey houses, lawns and driveways"></div>
    <h1 class="hero-title">Find your Local Property Manager</h1>
    <form class="search-panel">
      <span class="field-label label-type">Select Your Property Type</span>
      <div class="select-box">Single Home or Condo (Valued up to $300K)</div>
      <span class="field-label label-zip">In Zipcode</span>
      <div class="zip-input"></div>
      <div class="search-button">
        <svg width="14" height="14" viewBox="0 0 14 14"><circle cx="5.5" cy="5.5" r="4" fill="none" stroke="#fbc30a" stroke-width="2"/><line x1="8.5" y1="8.5" x2="13" y2="13" stroke="#fbc30a" stroke-width="2.4" stroke-linecap="round"/></svg>
        Search Now
      </div>
    </form>
    <p class="hero-note">Search our directory to find experienced and professional property management companies that meet your needs.</p>
  </section>

  <h2 class="steps-heading">To find property management companies <span>near you</span>:</h2>

  <div class="step-icon" style="left:174px">
    <svg width="54" height="40" viewBox="0 0 54 40">
      <path d="M14 18 L24 9 L34 18 V29 H14 Z" fill="#fbc30a" stroke="#4e4c4d" stroke-width="2"/>
      <rect x="21" y="21" width="6" height="8" fill="#4e4c4d"/>
      <path d="M2 30 Q10 26 18 32 H34 Q42 28 52 24 Q48 36 34 38 H10 Q4 36 2 30 Z" fill="#4e4c4d"/>
    </svg>
  </div>
  <svg class="step-arrow" style="left:377px" width="50" height="22" viewBox="0 0 50 22"><path d="M2 12 H46 M36 3 L47 11 L36 19" fill="none" stroke="#4e4c4d" stroke-width="2.5" stroke-linecap="round"/><line x1="10" y1="14" x2="40" y2="13" stroke="#fbc30a" stroke-width="2"/></svg>

  <div class="step-icon" style="left:553px">
    <svg width="50" height="44" viewBox="0 0 50 44">
      <rect x="4" y="4" width="26" height="32" fill="#fff" stroke="#fbc30a" stroke-width="2"/>
      <line x1="9" y1="12" x2="25" y2="12" stroke="#fbc30a" stroke-width="2"/>
      <line x1="9" y1="18" x2="21" y2="18" stroke="#fbc30a" stroke-width="2"/>
      <line x1="9" y1="24" x2="19" y2="24" stroke="#fbc30a" stroke-width="2"/>
      <circle cx="30" cy="24" r="9" fill="none" stroke="#4e4c4d" stroke-width="3"/>
      <line x1="37" y1="31" x2="46" y2="41" stroke="#4e4c4d" stroke-width="5" stroke-linecap="round"/>
    </svg>
  </div>
  <svg class="step-arrow" style="left:767px" width="50" height="22" viewBox="0 0 50 22"><path d="M2 12 H46 M36 3 L47 11 L36 19" fill="none" stroke="#4e4c4d" stroke-width="2.5" stroke-linecap="round"/><line x1="10" y1="14" x2="40" y2="13" stroke="#fbc30a" stroke-width="2"/></svg>

  <div class="step-icon" style="left:917px">
    <svg width="50" height="44" viewBox="0 0 50 44">
      <circle cx="25" cy="10" r="7" fill="#fbc30a"/>
      <path d="M14 40 V26 Q14 19 25 19 Q36 19 36 26 V40 Z" fill="#fbc30a"/>
      <circle cx="13" cy="18" r="5" fill="#4e4c4d"/>
      <path d="M4 40 V30 Q4 25 13 25 Q20 25 20 30 V40 Z" fill="#4e4c4d"/>
      <circle cx="39" cy="22" r="4" fill="#4e4c4d"/>
      <path d="M32 40 V33 Q32 29 39 29 Q46 29 46 33 V40 Z" fill="#4e4c4d"/>
    </svg>
  </div>

  <p class="step-caption" style="left:38px">Select your property type and zipcode</p>
  <p class="step-caption" style="left:416px">Review property manager listings in your area</p>
  <p class="step-caption" style="left:781px">Select and compare property managers</p>
</body>
</html>
```